Change the world and help build SpinLOOM.tv!

We need a mobile website design for our Beta release - see wireframes attached.
See our Logo design files attached along with fonts, etc.
Please see enclosed .PDF that provides a great overview of our company, LOOM.
Any questions, feel free to ask - we're very engaged here on Sketch Hive and will make ourselves available.
Thanks!
Tobias
Updates
Very pleased with what's coming in! Would like to see some more variety and more volume of designs.
Target Market(s)
Ages 13+ (all genders, races, creeds, income levels, etc)
Coding
Coded - Design and coding required
Number of Pages Required
5+ page
Font styles to use
Colors
Designer to choose colors to be used in the design.
Look and feel
Each slider illustrates characteristics of the customer's brand and the style your logo design should communicate.

```html
<!DOCTYPE html>
<html lang="en">
<head>
<meta charset="utf-8">
<title>SpinLOOM.tv – Join Beta</title>
<link href="https://fonts.googleapis.com/css2?family=League+Gothic:wdth@75..100&family=Montserrat:wght@500;600&family=Roboto:wght@400&display=swap" rel="stylesheet">
<style>
  :root {
    --navy: #263358;
    --sky: #69b8d3;
    --ink: #222222;
    --text: #3a3a3a;
    --rule: #dddddd;
    --white: #ffffff;
  }
  * { box-sizing: border-box; margin: 0; padding: 0; }
  html, body { width: 1200px; height: 916px; overflow: hidden; background: var(--white); }
  body { position: relative; font-family: "Roboto", Arial, sans-serif; color: var(--text); }

  .site-header { position: absolute; left: 0; top: 0; width: 1200px; height: 102px; background: var(--white); }
  .header-panel { position: absolute; left: 0; top: 0; }
  .brand { position: absolute; left: 18px; top: 41px; display: flex; align-items: center; gap: 6px;
    font-family: "Montserrat", sans-serif; font-weight: 600; font-size: 16px; line-height: 20px; color: var(--navy); }
  .brand-dot { width: 10px; height: 10px; border-radius: 50%; background: var(--sky); flex: none; }

  .campaign-call { position: absolute; left: 170px; top: 9px; font-family: "League Gothic", sans-serif;
    font-stretch: 75%; font-variation-settings: "wdth" 75; font-size: 42px; line-height: 40px; color: var(--navy); }
  .campaign-call .accent { color: var(--sky); }

  .main-nav { position: absolute; left: 902px; top: 29px; display: flex; gap: 50px; }
  .main-nav a { font-family: "Montserrat", sans-serif; font-weight: 600; font-size: 19px; line-height: 23px; color: var(--white); text-decoration: none; }
  .main-nav a:last-child { margin-left: 30px; }

  .hero { position: absolute; left: 0; top: 102px; width: 1200px; height: 148px;
    background: linear-gradient(90deg, #1d3038 0%, #2f5360 28%, #233c44 52%, #1e3a33 75%, #2b4a44 100%); }

  .signup { position: absolute; left: 0; top: 250px; width: 1200px; text-align: center; }
  .signup-title { margin-top: 43px; font-family: "Montserrat", sans-serif; font-weight: 600; font-size: 42px; line-height: 50px; color: var(--ink); }
  .signup-rule { width: 57px; height: 5px; background: var(--sky); margin: 4px auto 0; }
  .signup-intro { margin: 22px auto 0; width: 720px; font-size: 13.8px; line-height: 20px; letter-spacing: 0.4px; color: var(--text); }

  .signup-form { position: absolute; left: 202px; top: 440px; width: 797px; }
  .field { position: absolute; width: 380px; height: 44px; }
  .field label { position: absolute; left: 0; top: 6px; font-family: Arial, Helvetica, sans-serif; font-size: 12.5px; color: #444; }
  .row-3 label { top: 12px; }
  .field .line { position: absolute; left: 0; bottom: 0; width: 100%; height: 4px; background: var(--rule); }
  .col-left { left: 0; }
  .col-right { left: 417px; }
  .row-1 { top: 0; }
  .row-2 { top: 69px; }
  .row-3 { top: 146px; }
  .grip { position: absolute; right: 0; top: 1px; }

  .register-btn { position: absolute; left: 0; top: 222px; width: 797px; height: 53px; border: none;
    background: var(--sky); color: var(--white); font-family: Arial, Helvetica, sans-serif; font-weight: bold;
    font-size: 16.5px; letter-spacing: 1.6px; }

  .site-footer { position: absolute; left: 0; top: 838px; width: 1200px; height: 78px; background: var(--navy);
    display: flex; justify-content: center; align-items: center; gap: 22px;
    font-family: "Montserrat", sans-serif; font-weight: 500; font-size: 17.5px; color: var(--white); }
  .site-footer a { color: var(--white); text-decoration: none; }
</style>
</head>
<body>
  <header class="site-header">
    <svg class="header-panel" width="1200" height="102" viewBox="0 0 1200 102">
      <polygon points="712,0 1200,0 1200,102 654,102" fill="var(--navy)"/>
    </svg>
    <div class="brand"><span class="brand-dot"></span>SpinLOOM.tv</div>
    <p class="campaign-call">HELP OUR CAUSE AND DONATE<br>TO OUR <span class="accent">FUNDRIVER CAMPAIGN!</span></p>
    <nav class="main-nav">
      <a href="#">JOIN<br>BETA</a>
      <a href="#">ARTIST<br>SIGN-UP</a>
    </nav>
  </header>

  <div class="hero" role="img" aria-label="Dimmed photo of a camera monitor on a film set with a microphone in the foreground"></div>

  <section class="signup">
    <h1 class="signup-title">JOIN BETA</h1>
    <div class="signup-rule"></div>
    <p class="signup-intro">Sing-up to receive an invitation to join our pre-launch (Beta) version of LOOM! Join our growing community of mental health warriors and help build a platform that can improve the lives of millions of people.</p>
  </section>

  <form class="signup-form">
    <div class="field col-left row-1"><label>Name</label><span class="line"></span></div>
    <div class="field col-right row-1"><label>Date of birth</label><span class="line"></span></div>
    <div class="field col-left row-2"><label>Address</label><span class="line"></span></div>
    <div class="field col-right row-2"><label>Email</label><span class="line"></span></div>
    <div class="field col-left row-3"><label>Phone</label><span class="line"></span></div>
    <div class="field col-right row-3"><label>Share your story with us</label>
      <svg class="grip" width="27" height="27" viewBox="0 0 27 27" fill="#cfcfcf">
        <rect x="21" y="0" width="6" height="6"/>
        <rect x="12" y="9" width="6" height="6"/><rect x="21" y="9" width="6" height="6"/>
        <rect x="3" y="18" width="6" height="6"/><rect x="12" y="18" width="6" height="6"/><rect x="21" y="18" width="6" height="6"/>
      </svg>
      <span class="line"></span></div>
    <button type="button" class="register-btn">REGISTER</button>
  </form>

  <footer class="site-footer">
    <a href="#">Terms and Conditions</a><span>|</span>
    <a href="#">Privacy Policy</a><span>|</span>
    <a href="#">About LOOM</a><span>|</span>
    <a href="#">The LOOM Team</a>
  </footer>
</body>
</html>
```